Take your idea to next level of implementation

Need a website for the training program that we are launching. Maple Crest Path is training provided to aspiring entrepreneurs.
The training comprises of business skills imparted to participants in order to help them develop their ideas and take the ideas to the next level of implementation.
The training program will be conducted in 8 sessions spanning over 5 months.

Coding

Coded - Design and coding required

Number of Pages Required

1 page

Colors

Designer to choose colors to be used in the design.

Requirements
Must have
• The project must have single page
Nice to have
• It would be nice to have a landing page that feels positive and will attract applicants.
• It should be highly professional.
Should not have
• Pictures used in the template should not have any people.

```html
<!DOCTYPE html>
<html lang="en">
<head>
<meta charset="utf-8">
<title>Maple Crest Path</title>
<link href="https://fonts.googleapis.com/css2?family=Josefin+Sans:wght@700&family=Open+Sans:wght@400;600;700&display=swap" rel="stylesheet">
<style>
:root{
  --navy:#2c3a66;
  --navy-deep:#1f2b52;
  --orange:#f47b50;
  --ink:#3b3f4a;
  --muted:#7c818c;
  --paper:#ffffff;
  --mist:#e9eaec;
  --stage:#eef0f2;
  --footer:#2f3237;
  --rule:#dfe1e5;
}
*{box-sizing:border-box;margin:0;padding:0}
html,body{width:1200px;height:5220px;overflow:hidden;background:var(--stage)}
body{position:relative;font-family:"Open Sans",Arial,sans-serif;color:var(--ink)}
.head{font-family:"Josefin Sans",Arial,sans-serif;font-weight:700;text-transform:uppercase;color:var(--navy);letter-spacing:.5px}
.brand{display:flex;align-items:center;gap:10px}
.brand-dot{border-radius:50%;background:var(--navy);flex:none}
.btn{display:inline-block;background:var(--orange);color:#fff;font-weight:700;border-radius:20px;text-align:center}
.pill{display:inline-block;background:var(--navy);color:#fff;font-family:"Josefin Sans",Arial,sans-serif;font-weight:700;text-transform:uppercase;border-radius:30px;text-align:center}
.photo{position:absolute;inset:0}

/* page-side brand */
.side-brand{position:absolute;left:72px;top:30px}
.side-brand .name{font-size:30px;line-height:1.05;width:220px}
.side-brand .brand-dot{width:40px;height:40px}

/* ---------- desktop ---------- */
.desktop{position:absolute;left:400px;top:40px;width:760px;height:5060px;background:var(--paper);overflow:hidden;box-shadow:0 2px 10px rgba(0,0,0,.06)}
.d-sec{position:absolute;left:0;width:760px;overflow:hidden}
.d-hero{top:0;height:360px}
.d-hero .photo{background:linear-gradient(180deg,#d9dadc 0%,#eeeeef 55%,#c9cbce 100%)}
.d-nav{position:absolute;top:14px;left:24px;right:24px;display:flex;align-items:center;justify-content:space-between}
.d-nav .brand .name{font-size:15px;line-height:1;width:110px}
.d-nav .brand-dot{width:20px;height:20px}
.d-nav ul{display:flex;gap:14px;list-style:none;font-size:8px;color:var(--ink);align-items:center}
.d-nav .btn{font-size:8px;padding:5px 18px}
.d-hero .inner{position:absolute;top:80px;left:120px;width:520px;text-align:center}
.d-hero h1{font-size:34px;margin-bottom:14px}
.d-hero p{font-size:8.5px;line-height:1.55;color:var(--ink)}
.d-hero .call{font-size:10px;margin:22px 0 14px}
.d-hero .btn{font-size:9px;padding:6px 26px}
.d-hero .pill{font-size:11px;padding:10px 34px;margin-top:14px}

.d-prog{top:360px;height:680px}
.d-prog .photo{background:linear-gradient(135deg,#cfd1d4 0%,#e4d99a 45%,#f2e27a 60%,#c8c9cb 100%)}
.card{position:absolute;background:#fff;box-shadow:0 4px 18px rgba(0,0,0,.12)}
.d-prog .card{left:32px;top:200px;width:350px;padding:30px 26px}
.d-prog h2{font-size:30px;margin-bottom:16px}
.d-prog h3{font-size:11px;line-height:1.4;margin-bottom:12px}
.d-prog p{font-size:8px;line-height:1.6;margin-bottom:10px}
.d-prog .btn{font-size:8px;padding:5px 20px;margin-top:6px}

.d-why{top:1050px;height:340px;background:var(--navy);text-align:center;color:#fff}
.d-why .photo{background:linear-gradient(180deg,rgba(60,75,120,.7),rgba(31,43,82,.95))}
.d-why .inner{position:relative;padding:58px 140px 0}
.d-why h2{color:#fff;font-size:30px;margin-bottom:22px}
.d-why p{font-size:8px;line-height:1.6;margin-bottom:10px;color:#e4e7ef}
.d-why .btn{font-size:8px;padding:5px 22px;margin-top:10px}

.d-faq{top:1390px;height:1780px;padding:50px 50px 0}
.d-faq h2{font-size:32px;margin-bottom:28px}
.faq{border-bottom:1px solid var(--rule);padding:10px 0 12px}
.d-faq .faq h4{font-size:9.5px;font-weight:700;color:var(--navy);text-transform:uppercase;margin-bottom:7px;font-family:"Open Sans",Arial,sans-serif}
.d-faq .faq p{font-size:8px;line-height:1.6;color:var(--muted);margin-bottom:5px}

.d-acad{top:3175px;height:470px;background:var(--navy);text-align:center}
.d-acad .photo{background:linear-gradient(180deg,rgba(70,85,130,.6),rgba(31,43,82,.95))}
.d-acad .inner{position:relative;padding:68px 150px 0}
.d-acad h2{color:#fff;font-size:30px;margin-bottom:18px}
.d-acad p{font-size:8px;line-height:1.6;color:#e4e7ef;margin-bottom:20px}
.badges{display:flex;justify-content:center;gap:12px;margin-bottom:18px}
.badge{background:#fff;display:flex;align-items:center;justify-content:center}
.badge span{display:block;background:var(--mist)}
.d-acad .badge{width:120px;height:62px}
.d-acad .badge span{width:70px;height:34px}
.d-acad .pill{font-size:11px;padding:10px 34px;margin-bottom:16px}
.d-acad .btn{font-size:8px;padding:5px 22px}

.d-people{top:3665px;height:605px;padding:30px 50px 0}
.d-people h2{font-size:30px;margin-bottom:30px}
.people{display:grid;grid-template-columns:1fr 1fr;row-gap:34px;column-gap:40px}
.person{display:flex;align-items:center;gap:16px}
.avatar{border-radius:50%;background:linear-gradient(135deg,#c9ccd2,#9aa0ab);flex:none}
.d-people .avatar{width:74px;height:74px}
.d-people .person h5{font-size:10px;font-weight:700;color:var(--navy);text-transform:uppercase;margin-bottom:4px}
.d-people .person p{font-size:8px;line-height:1.5;color:var(--muted)}

.d-apply{top:4270px;height:550px;text-align:center}
.d-apply .photo{background:linear-gradient(180deg,#e3e4e6,#cfd1d4 60%,#dcdde0)}
.d-apply .inner{position:relative;padding:44px 0 0}
.d-apply h2{font-size:30px;margin-bottom:12px}
.d-apply p{font-size:8px;line-height:1.6;width:460px;margin:0 auto 22px}
.form{background:#fff;margin:0 auto;text-align:left}
.d-apply .form{width:240px;padding:22px 24px}
.field{border-bottom:1px solid var(--rule);color:var(--muted)}
.d-apply .field{font-size:8px;padding:10px 0 5px;margin-bottom:8px}
.d-apply .form .btn{display:block;width:70px;margin:18px auto 0;font-size:8px;padding:5px 0}

.d-foot{top:4820px;height:240px;background:var(--footer);text-align:center;color:#c6c9cf}
.foot-brand{justify-content:center}
.foot-brand .name{color:#fff}
.foot-brand .brand-dot{background:#fff}
.d-foot .foot-brand{padding-top:44px}
.d-foot .foot-brand .name{font-size:16px;width:110px;text-align:left;line-height:1}
.d-foot .foot-brand .brand-dot{width:22px;height:22px}
.socials{display:flex;justify-content:center;gap:8px}
.socials span{border-radius:50%;background:#8d929b}
.d-foot .socials{margin:20px 0 14px}
.d-foot .socials span{width:16px;height:16px}
.d-foot .mail{font-size:8px}
.d-foot .copy{font-size:7px;margin-top:42px;color:#8d929b}

/* ---------- mobile ---------- */
.mobile{position:absolute;left:72px;top:176px;width:308px;height:3710px;background:var(--paper);overflow:hidden;box-shadow:0 2px 10px rgba(0,0,0,.06)}
.m-sec{position:absolute;left:0;width:308px;overflow:hidden}
.m-hero{top:0;height:215px;text-align:center}
.m-hero .photo{background:linear-gradient(180deg,#dcdddf,#eeeeef 60%,#cdcfd2)}
.m-hero .top{position:absolute;top:10px;left:12px;right:12px;display:flex;justify-content:space-between;align-items:center}
.m-hero .brand .name{font-size:9px;width:64px;line-height:1}
.m-hero .brand-dot{width:12px;height:12px}
.burger{width:14px;height:10px;border-top:2px solid var(--navy);border-bottom:2px solid var(--navy);position:relative}
.burger::after{content:"";position:absolute;left:0;right:0;top:2px;border-top:2px solid var(--navy)}
.m-hero .inner{position:relative;padding:56px 26px 0}
.m-hero h1{font-size:17px;margin-bottom:8px}
.m-hero p{font-size:6px;line-height:1.5}
.m-hero .btn{font-size:6px;padding:3px 16px;margin-top:10px}
.m-hero .pill{font-size:6px;padding:5px 14px;margin-top:8px}

.m-prog{top:215px;height:490px}
.m-prog .photo{background:linear-gradient(135deg,#d2d3d6,#ead98a 50%,#f0e07a 65%,#cdced1)}
.m-prog .card{left:0;top:0;width:170px;padding:28px 14px 18px;height:490px}
.m-prog h2{font-size:16px;margin-bottom:10px}
.m-prog h3{font-size:7px;line-height:1.4;margin-bottom:8px}
.m-prog p{font-size:5.5px;line-height:1.6;margin-bottom:7px}
.m-prog .btn{font-size:5.5px;padding:3px 14px}

.m-why{top:715px;height:305px;background:var(--navy);text-align:center}
.m-why .photo{background:linear-gradient(180deg,rgba(60,75,120,.7),rgba(31,43,82,.95))}
.m-why .inner{position:relative;padding:34px 26px 0}
.m-why h2{color:#fff;font-size:16px;margin-bottom:12px}
.m-why p{font-size:5.5px;line-height:1.6;color:#e4e7ef;margin-bottom:7px}
.m-why .btn{font-size:5.5px;padding:3px 14px;margin-top:6px}

.m-faq{top:1020px;height:1435px;padding:26px 16px 0}
.m-faq h2{font-size:16px;margin-bottom:14px}
.m-faq .faq{padding:7px 0 8px}
.m-faq .faq h4{font-size:6px;font-weight:700;color:var(--navy);text-transform:uppercase;margin-bottom:4px;font-family:"Open Sans",Arial,sans-serif}
.m-faq .faq p{font-size:5.5px;line-height:1.55;color:var(--muted)}

.m-acad{top:2460px;height:285px;background:var(--navy);text-align:center}
.m-acad .photo{background:linear-gradient(180deg,rgba(70,85,130,.6),rgba(31,43,82,.95))}
.m-acad .inner{position:relative;padding:30px 24px 0}
.m-acad h2{color:#fff;font-size:16px;margin-bottom:10px}
.m-acad p{font-size:5.5px;line-height:1.6;color:#e4e7ef;margin-bottom:12px}
.m-acad .badge{width:70px;height:38px}
.m-acad .badge span{width:42px;height:20px}
.m-acad .badges{margin-bottom:10px}
.m-acad .pill{font-size:6px;padding:5px 14px;margin-bottom:8px}
.m-acad .btn{font-size:5.5px;padding:3px 14px}

.m-people{top:2765px;height:430px;padding:20px 22px 0}
.m-people h2{font-size:16px;margin-bottom:14px}
.m-people .list{display:flex;flex-direction:column;gap:16px}
.m-people .avatar{width:42px;height:42px}
.m-people .person{gap:10px}
.m-people .person h5{font-size:6.5px;font-weight:700;color:var(--navy);text-transform:uppercase;margin-bottom:2px}
.m-people .person p{font-size:5.5px;line-height:1.4;color:var(--muted)}

.m-apply{top:3200px;height:345px;text-align:center}
.m-apply .photo{background:linear-gradient(180deg,#e3e4e6,#d0d2d5 60%,#dcdde0)}
.m-apply .inner{position:relative;padding:24px 0 0}
.m-apply h2{font-size:16px;margin-bottom:8px}
.m-apply p{font-size:5.5px;line-height:1.5;width:240px;margin:0 auto 12px}
.m-apply .form{width:200px;padding:14px 16px}
.m-apply .field{font-size:5.5px;padding:8px 0 3px;margin-bottom:6px}
.m-apply .form .btn{display:block;width:46px;margin:12px auto 0;font-size:5.5px;padding:3px 0}

.m-foot{top:3545px;height:165px;background:var(--footer);text-align:center;color:#c6c9cf}
.m-foot .foot-brand{padding-top:26px}
.m-foot .foot-brand .name{font-size:10px;width:70px;text-align:left;line-height:1}
.m-foot .foot-brand .brand-dot{width:14px;height:14px}
.m-foot .socials{margin:12px 0 8px}
.m-foot .socials span{width:11px;height:11px}
.m-foot .mail{font-size:5.5px}
.m-foot .copy{font-size:5px;margin-top:28px;color:#8d929b}
</style>
</head>
<body>

<div class="side-brand brand"><span class="brand-dot"></span><span class="name head">Maple Crest Path</span></div>

<!-- desktop layout -->
<main class="desktop">
  <section class="d-sec d-hero">
    <div class="photo" role="img" aria-label="Soft grey view of a bright staircase"></div>
    <nav class="d-nav">
      <div class="brand"><span class="brand-dot"></span><span class="name head">Maple Crest Path</span></div>
      <ul><li>Home</li><li>The Lab</li><li>Programme</li><li>Why This Lab</li><li>FAQs</li><li>Academic Support</li><li><span class="btn">Apply</span></li></ul>
    </nav>
    <div class="inner">
      <h1 class="head">Maple Crest Path</h1>
      <p>Maple Crest Path is a training programme for aspiring entrepreneurs who want to turn an idea into a working venture. Over eight sessions spread across five months, participants build the business skills needed to test, shape and launch their ideas with guidance from experienced faculty.</p>
      <p class="call head">To apply for the first edition of this project</p>
      <span class="btn">Apply</span><br>
      <span class="pill">The training is completely free of charge</span>
    </div>
  </section>

  <section class="d-sec d-prog">
    <div class="photo" role="img" aria-label="Wall of yellow sticky notes from a planning session"></div>
    <div class="card">
      <h2 class="head">Programme</h2>
      <h3 class="head">Do you have an idea?<br>What next?</h3>
      <p>The programme helps you take an early idea and move it step by step toward implementation. Sessions cover customer discovery, testing assumptions, building a simple business model and preparing a clear plan for the months ahead.</p>
      <p>Each session mixes short lectures with hands-on work on your own idea, so you leave every meeting with concrete progress and next steps you can act on straight away.</p>
      <p>The training runs in 8 sessions over 5 months and is open to founders at the very first stage of their journey, before or just after forming a team.</p>
      <span class="btn">Apply</span>
    </div>
  </section>

  <section class="d-sec d-why">
    <div class="photo" role="img" aria-label="Faint navy-toned view of a workspace"></div>
    <div class="inner">
      <h2 class="head">Why Maple Crest Path?</h2>
      <p>The programme is built on a proven method for testing ideas scientifically, helping founders make better decisions with less time and money wasted on plans that do not hold up.</p>
      <p>Participants learn from faculty who combine research with years of work alongside young ventures, and they join a peer group facing the same early questions.</p>
      <p>Most of all, it gives you structure, feedback and a deadline to keep moving forward.</p>
      <span class="btn">Apply</span>
    </div>
  </section>

  <section class="d-sec d-faq">
    <h2 class="head">FAQs</h2>
    <div class="faq"><h4>What is the objective of training programme?</h4><p>The programme aims to give aspiring entrepreneurs the skills to evaluate and develop their ideas, so that they can take them to the next level of implementation with confidence and a clear method.</p><p>It focuses on practical tools rather than theory alone.</p></div>
    <div class="faq"><h4>When and where is the Maple Crest Path training offered?</h4><p>The training is held in 8 sessions spread over 5 months at our partner campus in Riverton. Each session lasts one full day and dates are shared with selected participants well in advance.</p><p>Sessions are scheduled on weekends so that working applicants can attend without leaving their jobs.</p><p>A detailed calendar is sent with the acceptance letter.</p></div>
    <div class="faq"><h4>What is the fee for the training programme?</h4><p>There is no fee. The training is completely free of charge for all selected participants.</p></div>
    <div class="faq"><h4>I do not live in Riverton, do I worry about travel and accommodation?</h4><p>Participants arrange their own travel and stay. We can share a list of nearby options on request.</p></div>
    <div class="faq"><h4>What is the content of training program?</h4><p>Sessions cover problem definition, customer interviews, value proposition, business models, testing hypotheses, basic finance and pitching. Every topic is applied directly to your own idea during the session.</p><p>Between sessions you complete short tasks that keep your idea moving forward.</p></div>
    <div class="faq"><h4>Is it compulsory to attend all sessions?</h4><p>Yes. Each session builds on the previous one, so full attendance is required to complete the programme and receive the certificate.</p><p>Missing more than one session may lead to removal from the group.</p></div>
    <div class="faq"><h4>What is the class size?</h4><p>Each cohort is kept small, around thirty participants, so that everyone receives personal feedback from the faculty.</p></div>
    <div class="faq"><h4>Who are going to be the instructors/facilitators for the business support programme?</h4><p>Sessions are led by faculty from our academic partners, supported by mentors who have built and advised early ventures.</p></div>
    <div class="faq"><h4>Who are eligible to join the programme?</h4><p>Anyone with an early business idea who is ready to commit time over five months can apply, regardless of background.</p></div>
    <div class="faq"><h4>What is the main purpose of the entrepreneur training programme?</h4><p>The main purpose is to help founders decide with evidence whether to pursue, change or drop an idea, and to give them a repeatable method they can use on any future venture.</p><p>It also supports research on how founders make early decisions.</p></div>
    <div class="faq"><h4>Is participation in the business support programme only open to founders and co-founders?</h4><p>Yes, the programme is designed for founders and co-founders who are actively working on their own idea.</p></div>
    <div class="faq"><h4>Will I be asked to share confidential information with the other members of my class?</h4><p>No. You decide how much of your idea to share. Exercises can be completed without revealing sensitive details.</p></div>
    <div class="faq"><h4>How will the data be used and their security be protected?</h4><p>Data collected during the programme is stored securely and used only in anonymous form for research and programme improvement. It is never sold or shared with third parties.</p></div>
  </section>

  <section class="d-sec d-acad">
    <div class="photo" role="img" aria-label="Faint navy-toned campus view"></div>
    <div class="inner">
      <h2 class="head">Academic Support</h2>
      <p>The programme is delivered with the support of two leading business schools, whose faculty designed the curriculum and lead the sessions throughout the five months.</p>
      <div class="badges"><div class="badge"><span></span></div><div class="badge"><span></span></div></div>
      <span class="pill">The training is completely free of charge</span><br>
      <span class="btn">Apply</span>
    </div>
  </section>

  <section class="d-sec d-people">
    <h2 class="head">People</h2>
    <div class="people">
      <div class="person"><div class="avatar" role="img" aria-label="Portrait of Ravi Menon"></div><div><h5>Ravi Menon</h5><p>Associate Professor of Strategy<br>Programme Lead</p></div></div>
      <div class="person"><div class="avatar" role="img" aria-label="Portrait of Leela Rao"></div><div><h5>Leela Rao</h5><p>Senior Researcher<br>Entrepreneurship Centre</p></div></div>
      <div class="person"><div class="avatar" role="img" aria-label="Portrait of Marco Fenton"></div><div><h5>Marco Fenton</h5><p>Professor of Management<br>Faculty Advisor</p></div></div>
      <div class="person"><div class="avatar" role="img" aria-label="Portrait of Paolo Dellavia"></div><div><h5>Paolo Dellavia</h5><p>Professor of Innovation<br>Faculty Advisor</p></div></div>
      <div class="person"><div class="avatar" role="img" aria-label="Portrait of Sara Lindqvist"></div><div><h5>Sara Lindqvist</h5><p>Assistant Professor<br>Session Instructor</p></div></div>
    </div>
  </section>

  <section class="d-sec d-apply">
    <div class="photo" role="img" aria-label="Soft grey view of an open office"></div>
    <div class="inner">
      <h2 class="head">How to apply</h2>
      <p>Fill in the short form below to apply for the first edition. Selected applicants will be contacted by email with the next steps and the session calendar.</p>
      <div class="form">
        <div class="field">Full name</div>
        <div class="field">Email</div>
        <div class="field">Phone</div>
        <div class="field">Your idea in one line</div>
        <span class="btn">Submit</span>
      </div>
    </div>
  </section>

  <footer class="d-sec d-foot">
    <div class="brand foot-brand"><span class="brand-dot"></span><span class="name head">Maple Crest Path</span></div>
    <div class="socials"><span></span><span></span><span></span><span></span></div>
    <p class="mail">hello@maplecrestpath.org</p>
    <p class="copy">© 2024 Maple Crest Path. All rights reserved.</p>
  </footer>
</main>

<!-- mobile layout -->
<main class="mobile">
  <section class="m-sec m-hero">
    <div class="photo" role="img" aria-label="Soft grey view of a bright staircase"></div>
    <div class="top"><div class="brand"><span class="brand-dot"></span><span class="name head">Maple Crest Path</span></div><div class="burger"></div></div>
    <div class="inner">
      <h1 class="head">Maple Crest Path</h1>
      <p>A free training programme for aspiring entrepreneurs, run in eight sessions over five months.</p>
      <span class="btn">Apply</span><br>
      <span class="pill">The training is completely free of charge</span>
    </div>
  </section>

  <section class="m-sec m-prog">
    <div class="photo" role="img" aria-label="Wall of yellow sticky notes from a planning session"></div>
    <div class="card">
      <h2 class="head">Programme</h2>
      <h3 class="head">Do you have an idea?<br>What next?</h3>
      <p>The programme helps you take an early idea and move it step by step toward implementation, from customer discovery to a clear plan.</p>
      <p>Each session mixes short lectures with hands-on work on your own idea, so you leave every meeting with real progress.</p>
      <p>The training runs in 8 sessions over 5 months and is open to founders at the very first stage of their journey.</p>
      <p>Places are limited, so apply early to secure a seat in the first edition.</p>
      <span class="btn">Apply</span>
    </div>
  </section>

  <section class="m-sec m-why">
    <div class="photo" role="img" aria-label="Faint navy-toned view of a workspace"></div>
    <div class="inner">
      <h2 class="head">Why Maple Crest Path?</h2>
      <p>The programme is built on a proven method for testing ideas, helping founders make better decisions with less waste.</p>
      <p>You learn from faculty with years of work alongside young ventures and join a peer group facing the same questions.</p>
      <span class="btn">Apply</span>
    </div>
  </section>

  <section class="m-sec m-faq">
    <h2 class="head">FAQs</h2>
    <div class="faq"><h4>What is the objective of training programme?</h4><p>To give aspiring entrepreneurs the skills to evaluate and develop their ideas and take them to the next level of implementation.</p></div>
    <div class="faq"><h4>When and where is the Maple Crest Path training offered?</h4><p>In 8 sessions over 5 months at our partner campus in Riverton, held on weekends. A full calendar comes with the acceptance letter.</p></div>
    <div class="faq"><h4>What is the fee for the training programme?</h4><p>There is no fee. The training is free for all selected participants.</p></div>
    <div class="faq"><h4>I do not live in Riverton, do I worry about travel and accommodation?</h4><p>Participants arrange their own travel and stay. We can share nearby options on request.</p></div>
    <div class="faq"><h4>What is the content of training program?</h4><p>Problem definition, customer interviews, value proposition, business models, testing hypotheses, basic finance and pitching, all applied to your own idea.</p></div>
    <div class="faq"><h4>Is it compulsory to attend all sessions?</h4><p>Yes. Each session builds on the last, so full attendance is needed to complete the programme.</p></div>
    <div class="faq"><h4>What is the class size?</h4><p>Around thirty participants per cohort, so everyone gets personal feedback.</p></div>
    <div class="faq"><h4>Who are going to be the instructors/facilitators for the business support programme?</h4><p>Faculty from our academic partners, supported by mentors who have built early ventures.</p></div>
    <div class="faq"><h4>Who are eligible to join the programme?</h4><p>Anyone with an early business idea ready to commit time over five months.</p></div>
    <div class="faq"><h4>What is the main purpose of the entrepreneur training programme?</h4><p>To help founders decide with evidence whether to pursue, change or drop an idea, using a method they can repeat.</p></div>
    <div class="faq"><h4>Is participation in the business support programme only open to founders and co-founders?</h4><p>Yes, it is designed for founders actively working on their own idea.</p></div>
    <div class="faq"><h4>Will I be asked to share confidential information with the other members of my class?</h4><p>No. You decide how much of your idea to share with the group.</p></div>
    <div class="faq"><h4>How will the data be used and their security be protected?</h4><p>Data is stored securely and used only in anonymous form for research and programme improvement.</p></div>
  </section>

  <section class="m-sec m-acad">
    <div class="photo" role="img" aria-label="Faint navy-toned campus view"></div>
    <div class="inner">
      <h2 class="head">Academic Support</h2>
      <p>Delivered with the support of two leading business schools whose faculty designed the curriculum.</p>
      <div class="badges"><div class="badge"><span></span></div><div class="badge"><span></span></div></div>
      <span class="pill">The training is completely free of charge</span><br>
      <span class="btn">Apply</span>
    </div>
  </section>

  <section class="m-sec m-people">
    <h2 class="head">People</h2>
    <div class="list">
      <div class="person"><div class="avatar" role="img" aria-label="Portrait of Ravi Menon"></div><div><h5>Ravi Menon</h5><p>Associate Professor of Strategy</p></div></div>
      <div class="person"><div class="avatar" role="img" aria-label="Portrait of Leela Rao"></div><div><h5>Leela Rao</h5><p>Senior Researcher</p></div></div>
      <div class="person"><div class="avatar" role="img" aria-label="Portrait of Marco Fenton"></div><div><h5>Marco Fenton</h5><p>Professor of Management</p></div></div>
      <div class="person"><div class="avatar" role="img" aria-label="Portrait of Paolo Dellavia"></div><div><h5>Paolo Dellavia</h5><p>Professor of Innovation</p></div></div>
      <div class="person"><div class="avatar" role="img" aria-label="Portrait of Sara Lindqvist"></div><div><h5>Sara Lindqvist</h5><p>Assistant Professor</p></div></div>
    </div>
  </section>

  <section class="m-sec m-apply">
    <div class="photo" role="img" aria-label="Soft grey view of an open office"></div>
    <div class="inner">
      <h2 class="head">How to apply</h2>
      <p>Fill in the short form below to apply for the first edition.</p>
      <div class="form">
        <div class="field">Full name</div>
        <div class="field">Email</div>
        <div class="field">Phone</div>
        <div class="field">Your idea in one line</div>
        <span class="btn">Submit</span>
      </div>
    </div>
  </section>

  <footer class="m-sec m-foot">
    <div class="brand foot-brand"><span class="brand-dot"></span><span class="name head">Maple Crest Path</span></div>
    <div class="socials"><span></span><span></span><span></span><span></span></div>
    <p class="mail">hello@maplecrestpath.org</p>
    <p class="copy">© 2024 Maple Crest Path</p>
  </footer>
</main>

</body>
</html>
```